Cadenza Elite Keyboard Academy is a comprehensive piano studio located in CBD area and provide individual piano lessons.

We also provide services for wedding organising band, or instrumental hiring or venue hiring, or organise concert to students.

I want my name card to be very creative, does not have to be the form or shape with the normal name card, can be in different shape. Also, I want the name card to be very upper class, because learning piano is a serious thing, so I do not want people to bargain with the prices. I want people to see it as a very elegant tuition so that they do not want to bargain and think it is worth to try.

Further more, Cadenza Elite Keyboard Academy is not like normal piano studio only provide piano lessons, we provide band services for each other event, such as cruise party, wedding etc. I want people to see it as owner of Elite Keyboard Academy, they will have different type of services all in one, I provide more than that, and I am well connected. I do not provide only piano lesson, but also all other musical knowledge and I am very professional

I want name card to be very simple, just name of company name, my name and website that's all, maybe phone number and email as well.

Please check my website to have more ideal concept.
http://harrietdowse.sitebuilder-example.com/cadenzakeyboard
Updates

Target Market(s)

For all people who love to play piano (better with upper class)

Industry/Entity Type

Wedding

Contact Information for Business Card

Harriet Dowse
Mobile:0418769052
Email: cadenzaelitekeys@mailbox-example.com

Colors

Designer to choose colors to be used in the design.

Requirements
Must have
• Creativity
Nice to have
• Black and white
some sort of piano image
Should not have
• Childish

```html
<!DOCTYPE html>
<html lang="en">
<head>
<meta charset="utf-8">
<title>Harriet Dowse – Cadenza Elite Keyboard Academy business card</title>
<link rel="stylesheet" href="https://fonts.googleapis.com/css2?family=Cinzel:wght@400;500&family=Open+Sans:wght@400;600&display=swap">
<style>
  :root {
    --bg: #e9e9e9;
    --card-white: #f7f7f7;
    --card-white-edge: #dcdcdc;
    --card-black: #121212;
    --card-black-glow: #262626;
    --ink-dark: #1a1a1a;
    --ink-mid: #444444;
    --ink-light: #f2f2f2;
    --rule-dark: #8a8a8a;
    --rule-light: #9c9c9c;
    --art-tone: #d9d9d9;
  }
  * { box-sizing: border-box; margin: 0; padding: 0; }
  html, body {
    width: 1200px; height: 878px; overflow: hidden;
    background: var(--bg);
  }
  .sheet {
    width: 1200px; height: 878px;
    display: flex; align-items: center; justify-content: center; gap: 40px;
  }
  .card {
    position: relative;
    width: 540px; height: 309px;
    box-shadow: 0 10px 28px rgba(0,0,0,.18);
    overflow: hidden;
  }
  .card--front {
    background: radial-gradient(ellipse at 40% 35%, #ffffff 0%, var(--card-white) 55%, var(--card-white-edge) 100%);
    color: var(--ink-dark);
  }
  .card--back {
    background: radial-gradient(ellipse at 50% 55%, var(--card-black-glow) 0%, var(--card-black) 70%);
    color: var(--ink-light);
  }
  .piano-art {
    position: absolute; left: 60px; top: 20px; width: 260px; height: 260px;
    border-radius: 50% 40% 45% 50%;
    background: radial-gradient(ellipse at center, var(--art-tone) 0%, rgba(217,217,217,0) 70%);
    opacity: .7;
  }
  .wordmark {
    position: absolute; left: 0; right: 0;
    display: flex; flex-direction: column; align-items: center;
  }
  .card--front .wordmark { top: 40px; }
  .card--back .wordmark { top: 112px; }
  .wordmark__rule {
    width: 400px; height: 0;
    border-top: 2px dotted var(--rule-dark);
    margin-bottom: 6px;
  }
  .card--back .wordmark__rule { border-top-color: var(--rule-light); }
  .wordmark__name {
    font-family: "Cinzel", serif; font-weight: 500;
    font-size: 44px; letter-spacing: 3px; line-height: 1;
  }
  .wordmark__tagline {
    font-family: "Cinzel", serif; font-weight: 400;
    font-size: 13px; letter-spacing: 6px; margin-top: 6px;
  }
  .contacts {
    position: absolute; left: 0; right: 0; top: 142px;
    display: flex; flex-direction: column; align-items: center; gap: 9px;
    font-family: "Open Sans", sans-serif;
  }
  .contact { text-align: center; }
  .contact__label {
    display: flex; align-items: center; justify-content: center; gap: 10px;
    font-size: 10px; font-weight: 600; letter-spacing: 1.5px; text-transform: uppercase;
    color: var(--ink-dark);
  }
  .contact__label::before, .contact__label::after {
    content: ""; width: 34px; border-top: 1px solid var(--ink-dark);
  }
  .contact__value {
    font-size: 10px; letter-spacing: .8px; text-transform: uppercase;
    color: var(--ink-mid); margin-top: 2px;
  }
</style>
</head>
<body>
<main class="sheet">
  <section class="card card--front" aria-label="Business card front">
    <div class="piano-art" role="img" aria-label="Faint grand piano line illustration"></div>
    <div class="wordmark">
      <div class="wordmark__rule"></div>
      <h1 class="wordmark__name">HARRIET DOWSE</h1>
      <p class="wordmark__tagline">CADENZA ELITE KEYBOARD ACADEMY</p>
    </div>
    <div class="contacts">
      <div class="contact">
        <p class="contact__label">Web Site</p>
        <p class="contact__value">harrietdowse.sitebuilder-example.com/cadenzakeyboard</p>
      </div>
      <div class="contact">
        <p class="contact__label">Email</p>
        <p class="contact__value">cadenzaelitekeys@mailbox-example.com</p>
      </div>
      <div class="contact">
        <p class="contact__label">Mobile</p>
        <p class="contact__value">+041 876 9052</p>
      </div>
    </div>
  </section>

  <section class="card card--back" aria-label="Business card back">
    <div class="wordmark">
      <div class="wordmark__rule"></div>
      <p class="wordmark__name">HARRIET DOWSE</p>
      <p class="wordmark__tagline">CADENZA ELITE KEYBOARD ACADEMY</p>
    </div>
  </section>
</main>
</body>
</html>
```